2 banner Designs

I have a trade show in Vegas and I want you to design 2 banners that are Graphic size: 33.5" (W) x 80.5" (H). The banners are standing in the booth.

I am looking for a luxury modern feel for the banners. The banners are going to be important to attract customers in.

I am showing latex foam pillows and latex mattress. The company is called Verdant Hush. Please use any photos from our website.

https://www.loomvaleny.net/verdanthush

Banner 1

Introducing our Verdant Hush mattress, a perfect harmony of luxurious organic cushioning and an advanced internal, zoned pressure-point support system.

Experience unparalleled back support and remarkable durability, all in one exceptional sleep solution.

Verdant Hush Mattress

GOTS-certified organic cotton
GOTS-certified organic wool
2 “ GOLS-certified organic latex
8” Pocket Coils
1’’ GOLS-certified organic latex

Banner 2

Verdant Hush Pillows

We developed a customizable pillow with the perfect amount of comfort and support.

Our New Latex pillow has an adjustable fill with 90% Natural Latex and 10% Traceable Wool.  Our pillow cover is made from GOTS-certified organic cotton.

FILE REQUIREMENTS
We can take the file in the following file formats:

Single Page PDF (Preferred)
JPG (Preferred)
PSD – Please flatten file
EPS – Please embed all images. Outline all fonts and strokes.
Ai – Please embed all images. Outline all fonts and strokes.
Don't Include Crop Marks or Bleed

Artwork at either full scale, 1/2 scale or 1/10 scale that is fine. Just make sure that when the file is being set up the DPI is compensated according to the scale.

Full Scale – 150 DPI
1/2 Scale – 300 DPI
1/10 Scale – 450 DPI
***Remove EVERYTHING from your file that you do not want printed on the final product - especially hidden layers and template guidelines.

- Flatten all Objects/Gradients/Swatches/Symbols/Special Effects/Transparencies
- Outline all text
- Flattened PDF (Single Page) or JPEG file types only
- Remove all crop marks/bleed otherwise they will be printed
- File must be the same exact size as what is ordered (exception is Gallery wrap Fold Edge and Products with templates)
- CMYK only (we do not print Pantone/5th/Spot/RGB)
- 150 dpi
- If using a template, the file uploaded to our site should match the exact "template size" (different than "graphic size").
- Do not scale template files, just flatten them and save at 150 dpi
- Files over 200" can be scaled
- Under 300 mb for upload

- Make sure all objects are embedded and flattened (we do not print Non-Native Art).
- If the file is made in Indesign, please flatten the file in Illustrator or Photoshop and export to a JPEG ONLY as we don't recommend using Indesign at our facility.

- If using Compound Paths to create transparencies/shapes, please completely rasterize or flatten them into the file or they may print incorrectly.

- We do not have specific measurements for Panel jobs. If you are printing in Panels, please make sure you are providing a minimum of 1" overlay in your files.

Please make sure that your file is in CMYK format for print production with no bleed. It is not required.

```html
<!DOCTYPE html>
<html lang="en">
<head>
<meta charset="utf-8">
<title>Verdant Hush – Trade Show Banners</title>
<link rel="stylesheet" href="https://fonts.googleapis.com/css2?family=Montserrat:wght@400;500;600;700;800;900&display=swap">
<style>
:root{
  --green:#5b8a26;
  --green-dark:#46701a;
  --charcoal:#454545;
  --charcoal-deep:#333333;
  --grey-mid:#6a6a6a;
  --page:#eeeeee;
  --white:#ffffff;
  --ink:#3a3a3a;
}
*{box-sizing:border-box;margin:0;padding:0}
html,body{width:1200px;height:2268px;overflow:hidden;background:var(--page);font-family:"Montserrat",Arial,sans-serif}
.stage{position:relative;width:1200px;height:2268px;display:flex;justify-content:center;align-items:center;gap:24px}
.banner{position:relative;width:570px;height:1370px;background:var(--white);overflow:hidden;box-shadow:0 10px 30px rgba(0,0,0,.18)}
.banner__header{position:absolute;left:0;top:0;width:100%;height:240px;background:radial-gradient(ellipse at 50% 30%,#5e5e5e 0%,var(--charcoal) 55%,var(--charcoal-deep) 100%)}
.brand{position:absolute;left:0;top:72px;width:100%;display:flex;flex-direction:column;align-items:center;gap:14px}
.brand__dot{width:42px;height:42px;border-radius:50%;border:3px solid var(--white)}
.brand__name{color:var(--white);font-weight:600;font-size:32px;letter-spacing:4px}
.photo{position:absolute}
.headline{position:absolute;left:0;width:100%;text-align:center}
.headline__intro{font-weight:700;font-size:22px;letter-spacing:3px;color:var(--ink)}
.headline__main{font-weight:900;font-size:82px;line-height:1;color:var(--green);letter-spacing:1px;margin-top:6px}
.headline__sub{font-weight:800;font-size:38px;line-height:1.1;color:var(--green);letter-spacing:1px}
.band{position:absolute;left:0;width:100%;background:var(--green);color:var(--white);display:flex;align-items:center;justify-content:center;text-align:center;padding:0 44px;font-size:17px;line-height:1.45;font-weight:500}
.bar{position:absolute;left:40px;right:40px;background:var(--charcoal);color:var(--white);display:flex;align-items:center;justify-content:center;font-weight:700;font-size:15px;letter-spacing:.5px;height:40px}
.lead{position:absolute;left:40px;right:40px;text-align:center;color:var(--green);font-weight:700;font-size:19px;line-height:1.35}
.features{position:absolute;left:20px;right:20px;display:flex;justify-content:space-between}
.feature{width:100px;display:flex;flex-direction:column;align-items:center;text-align:center;gap:8px}
.feature__label{font-size:11px;font-weight:600;color:var(--ink);line-height:1.3}
.coils{position:absolute;left:0;width:100%;height:52px;background:var(--green);color:var(--white);display:flex;align-items:center;justify-content:center;font-weight:800;font-size:24px}
.web{position:absolute;left:0;bottom:0;width:100%;height:92px;display:flex;align-items:center;justify-content:center;font-weight:800;font-size:26px;color:var(--charcoal);letter-spacing:1px;border-bottom:14px solid var(--green)}
.stats{position:absolute;left:40px;right:40px;display:flex;justify-content:center;align-items:center;gap:26px}
.stat{display:flex;align-items:center;gap:12px}
.stat__num{font-weight:900;font-size:52px;color:var(--charcoal)}
.stat__label{font-weight:800;font-size:17px;color:var(--green);line-height:1.15}
.stats__rule{width:2px;height:70px;background:#cfcfcf}
</style>
</head>
<body>
<main class="stage">

  <!-- Banner 1: mattress -->
  <section class="banner banner--mattress">
    <div class="banner__header"></div>
    <div class="brand"><span class="brand__dot"></span><span class="brand__name">VERDANT HUSH</span></div>

    <div class="photo" role="img" aria-label="Woman resting on a white pillow" style="left:30px;top:200px;width:250px;height:270px;background:linear-gradient(160deg,#d9d2c6,#a99e8c);border:5px solid var(--white)"></div>
    <div class="photo" role="img" aria-label="Woman sleeping in a bright bedroom" style="left:290px;top:200px;width:250px;height:270px;background:linear-gradient(160deg,#cfc8bd,#8f887c);border:5px solid var(--white)"></div>

    <svg class="photo" style="left:0;top:430px" width="570" height="200" viewBox="0 0 570 200" aria-hidden="true">
      <polygon points="0,60 285,0 570,60 570,200 0,200" fill="var(--green)"/>
      <polygon points="0,150 285,105 570,150 570,200 0,200" fill="var(--white)"/>
    </svg>
    <div class="photo" role="img" aria-label="Layered organic mattress" style="left:110px;top:470px;width:350px;height:140px;background:linear-gradient(180deg,#f6f6f4 0%,#e4e2dc 55%,#c9c5bb 100%);border-radius:8px"></div>

    <div class="headline" style="top:640px">
      <div class="headline__intro">INTRODUCING OUR</div>
      <div class="headline__main">VERDANT</div>
      <div class="headline__sub">HUSH MATTRESS</div>
    </div>

    <div class="band" style="top:840px;height:100px">A perfect harmony of luxurious organic cushioning and an advanced internal, zoned pressure-point support system.</div>

    <p class="lead" style="top:955px">Experience unparalleled back support and remarkable durability</p>
    <div class="bar" style="top:1012px">ALL IN ONE EXCEPTIONAL SLEEP SOLUTION</div>

    <div class="features" style="top:1070px">
      <div class="feature">
        <svg width="44" height="44" viewBox="0 0 44 44" aria-hidden="true"><circle cx="22" cy="22" r="20" fill="var(--green)"/><path d="M13 22l6 6 12-12" stroke="#fff" stroke-width="4" fill="none"/></svg>
        <span class="feature__label">GOTS-certified organic cotton</span>
      </div>
      <div class="feature">
        <svg width="44" height="44" viewBox="0 0 44 44" aria-hidden="true"><circle cx="22" cy="22" r="20" fill="var(--green)"/><path d="M13 22l6 6 12-12" stroke="#fff" stroke-width="4" fill="none"/></svg>
        <span class="feature__label">GOTS-certified organic wool</span>
      </div>
      <div class="feature">
        <svg width="44" height="44" viewBox="0 0 44 44" aria-hidden="true"><rect x="4" y="10" width="36" height="8" rx="2" fill="var(--green)"/><rect x="4" y="22" width="36" height="12" rx="2" fill="var(--green-dark)"/></svg>
        <span class="feature__label">2" GOLS-certified organic latex</span>
      </div>
      <div class="feature">
        <svg width="44" height="44" viewBox="0 0 44 44" aria-hidden="true"><path d="M6 8h32M6 36h32M10 8v28M22 8v28M34 8v28" stroke="var(--green)" stroke-width="4" fill="none"/></svg>
        <span class="feature__label">8" Pocket Coils</span>
      </div>
      <div class="feature">
        <svg width="44" height="44" viewBox="0 0 44 44" aria-hidden="true"><rect x="4" y="16" width="36" height="12" rx="2" fill="var(--green)"/></svg>
        <span class="feature__label">1" GOLS-certified organic latex</span>
      </div>
    </div>

    <div class="coils" style="top:1200px">8" Pocket Coils</div>
    <div class="web">www.loomvaleny.net</div>
  </section>

  <!-- Banner 2: pillows -->
  <section class="banner banner--pillows">
    <div class="banner__header"></div>
    <div class="brand"><span class="brand__dot"></span><span class="brand__name">VERDANT HUSH</span></div>

    <div class="photo" role="img" aria-label="Woman hugging a latex pillow in a warm bedroom" style="left:0;top:200px;width:570px;height:500px;background:linear-gradient(120deg,#b07a4c 0%,#d9c2a6 45%,#efe9e0 100%)"></div>
    <svg class="photo" style="left:0;top:590px" width="570" height="120" viewBox="0 0 570 120" aria-hidden="true">
      <polygon points="0,110 285,20 570,110 570,120 0,120" fill="var(--white)"/>
      <polyline points="0,100 285,10 570,100" stroke="var(--green)" stroke-width="8" fill="none"/>
    </svg>

    <div class="headline" style="top:715px">
      <div class="headline__intro">INTRODUCING OUR</div>
      <div class="headline__main">VERDANT</div>
      <div class="headline__sub">HUSH PILLOWS</div>
    </div>

    <div class="band" style="top:910px;height:86px">We developed a customizable pillow with the perfect amount of comfort and support.</div>
    <div class="bar" style="top:1012px;font-size:13px">OUR NEW LATEX PILLOW HAS AN ADJUSTABLE FILL WITH</div>

    <div class="stats" style="top:1070px">
      <div class="stat"><span class="stat__num">90%</span><span class="stat__label">NATURAL<br>LATEX</span></div>
      <span class="stats__rule"></span>
      <div class="stat"><span class="stat__num">10%</span><span class="stat__label">TRACEABLE<br>WOOL</span></div>
    </div>

    <div class="band" style="top:1170px;height:86px">Our pillow cover is made from GOTS-certified organic cotton</div>
    <div class="web">www.loomvaleny.net</div>
  </section>

</main>
</body>
</html>
```